Learning/tutoring center needs a postcard design.

I need a new postcard design for an established learning center. We have been in business for over 11 years. I want to stress how we are different from other centers. I want to include an offer for first time clients: $50.00 consultation for free
I also need two different postcards: one for public schools and one for private schools. The one for private will say that parents have the option of having our clinicians see children during their school day. The one for public schools will not say that. please visit the website to get an idea of what we offer and how we are different. brightpathtutoring.com
I am uploading my new logo and the new brochure. Let me know if you need anything else.

Target Market(s)

Parents of school age children- elementary or highschool

Industry/Entity Type

Business

Requirements
Must have
• My logo. Must look friendly and inviting. Must include the logo and colors should not be changed on the logo.
Nice to have
• Not looking specific to one race or ethinic background.

```html
<!DOCTYPE html>
<html lang="en">
<head>
<meta charset="utf-8">
<title>Brightpath Learning Center – Postcard</title>
<link href="https://fonts.googleapis.com/css2?family=Courgette&family=Open+Sans:ital,wght@0,400;0,600;0,700;1,600;1,700&display=swap" rel="stylesheet">
<style>
  :root {
    --purple: #6a2d8e;
    --lilac: #c7a0d0;
    --green: #8dc63f;
    --white: #ffffff;
    --ink-soft: #555555;
    --rule: #b9b9b9;
    --stage: #ebe8e4;
  }
  * { box-sizing: border-box; margin: 0; padding: 0; }
  html, body { width: 1080px; height: 1200px; overflow: hidden; }
  body { background: var(--stage); font-family: "Open Sans", sans-serif; position: relative; }

  .card { position: absolute; width: 860px; height: 556px; background: var(--white); overflow: hidden; box-shadow: 0 4px 12px rgba(0,0,0,.18); }
  .card--front { left: 40px; top: 40px; }
  .card--back { left: 180px; top: 620px; }

  .panel-shape { position: absolute; left: 0; top: 0; width: 860px; height: 506px; }

  .contact-band { position: absolute; left: 0; bottom: 0; width: 100%; height: 50px; background: var(--green); color: var(--white); display: flex; align-items: center; font-size: 19px; white-space: nowrap; }
  .contact-band .sep { display: inline-block; width: 1px; height: 24px; background: var(--white); margin: 0 12px; }
  .card--front .contact-band { padding-left: 28px; }
  .card--back .contact-band { padding-left: 42px; }

  .brand { position: absolute; display: flex; align-items: center; color: var(--purple); font-weight: 700; white-space: nowrap; }
  .brand-name { display: block; }
  .brand-dot { border-radius: 50%; background: var(--purple); flex: none; }
  .brand--front { left: 74px; top: 34px; font-size: 22px; line-height: 25px; gap: 12px; }
  .brand--front .brand-dot { width: 46px; height: 46px; }
  .brand--back { left: 550px; top: 28px; font-size: 12px; line-height: 14px; gap: 7px; }
  .brand--back .brand-dot { width: 26px; height: 26px; }

  .script { font-family: "Courgette", cursive; }
  .tagline { position: absolute; left: 40px; width: 350px; top: 110px; text-align: center; color: var(--purple); font-size: 17px; line-height: 21px; }

  .photo { position: absolute; }
  .photo--kids { left: 0; top: 160px; width: 404px; height: 346px; background: linear-gradient(160deg, #f1ede8 0%, #e8a79f 35%, #5cb870 60%, #3d5f9e 100%); }
  .photo--teens { left: 0; top: 140px; width: 516px; height: 216px; background: linear-gradient(100deg, #8a8f99 0%, #c79a7c 35%, #e8d0b4 60%, #2c2c32 100%); }

  .heading { position: absolute; color: var(--white); font-size: 22px; }
  .copy { position: absolute; color: var(--white); font-size: 12.4px; line-height: 18px; text-align: justify; }

  .offer { position: absolute; left: 470px; top: 214px; width: 356px; height: 72px; background: var(--white); border-radius: 8px; text-align: center; color: var(--purple); padding-top: 12px; }
  .offer-label { font-size: 14px; letter-spacing: .2px; }
  .offer-deal { font-size: 19px; margin-top: 4px; }
  .offer-note { position: absolute; left: 470px; width: 356px; top: 290px; text-align: center; color: var(--white); font-size: 12px; line-height: 15px; }

  .conditions-lead { position: absolute; left: 40px; top: 372px; color: var(--white); font-size: 12.4px; font-weight: 700; font-style: italic; }

  .return-address { position: absolute; left: 555px; top: 78px; font-size: 10.5px; line-height: 17px; color: var(--ink-soft); font-style: normal; }
  .stamp-box { position: absolute; left: 742px; top: 30px; width: 98px; height: 60px; border: 1px solid var(--rule); }
  .address-line { position: absolute; left: 590px; width: 250px; height: 1px; background: var(--rule); }
</style>
</head>
<body>

<section class="card card--front">
  <svg class="panel-shape" viewBox="0 0 860 506" aria-hidden="true">
    <path fill="var(--lilac)" d="M424 0 H860 V506 H424 Q404 506 404 486 V275 Q404 255 384 255 Q404 255 404 235 V20 Q404 0 424 0 Z"/>
    <path fill="var(--purple)" d="M440 0 H860 V506 H440 Q420 506 420 486 V275 Q420 255 400 255 Q420 255 420 235 V20 Q420 0 440 0 Z"/>
  </svg>

  <div class="brand brand--front"><span class="brand-dot"></span><span><span class="brand-name">Brightpath</span><span class="brand-name">Learning Center</span></span></div>
  <p class="tagline script">Results that Go Beyond<br>Traditional Tutoring</p>
  <div class="photo photo--kids" role="img" aria-label="Photo of three smiling schoolchildren wearing backpacks"></div>

  <h2 class="heading script" style="left:448px; top:40px;">Who We Are</h2>
  <p class="copy" style="left:443px; top:78px; width:390px;">Brightpath Learning Center has been helping families with their educational needs for more than 10 years. We are more than passionate about students’ success. At Brightpath you’ll find a welcoming environment, kind smiles and highly trained Learning Skills Specialists. Students will find a place where they will always be successful!</p>

  <div class="offer">
    <p class="offer-label">OFFER FOR FIRST TIME CLIENTS</p>
    <p class="offer-deal script">$50.00 consultation for Free</p>
  </div>
  <p class="offer-note script">Parents have the option of having our clinicians see<br>children during their school day</p>

  <h2 class="heading script" style="left:450px; top:334px;">How Can We Help?</h2>
  <p class="copy" style="left:443px; top:370px; width:390px;">At Brightpath Learning Center our primary goal is to diagnose the underlying cause for why a student may not be doing well in school. We don’t want to put a temporary bandage on the problem; we want to eliminate the problem. Our job is to make sure children are successful learners. We want them to have confidence and realize their potential.</p>

  <footer class="contact-band">brightpathtutoring.com<span class="sep"></span>555-014-2290<span class="sep"></span>info@BrightpathTutoring.com</footer>
</section>

<section class="card card--back">
  <svg class="panel-shape" viewBox="0 0 860 506" aria-hidden="true">
    <path fill="var(--lilac)" d="M0 0 H510 Q530 0 530 20 V230 Q530 250 550 250 Q530 250 530 270 V486 Q530 506 510 506 H0 Z"/>
    <path fill="var(--purple)" d="M0 0 H496 Q516 0 516 20 V230 Q516 250 536 250 Q516 250 516 270 V486 Q516 506 496 506 H0 Z"/>
  </svg>

  <h2 class="heading script" style="left:40px; top:28px;">Who Can We Help?</h2>
  <p class="copy" style="left:40px; top:66px; width:456px;">We work with students of all ages who have challenges with listening, language and communication, reading, spelling, writing, comprehension, math, organization and study skills, and/or attention and concentration.</p>

  <div class="photo photo--teens" role="img" aria-label="Photo of four smiling teenage students standing together"></div>

  <p class="conditions-lead">At Brightpath we can help all kinds of minds including:</p>
  <p class="copy" style="left:40px; top:398px; width:456px;">Anxiety Problems; Attention Deficit Hyperactivity Disorder; Auditory Processing Issues; Language Processing Issues; Autism spectrum Disorders; Developmental Delays; Dyslexia; Executive Function Weakness; Learning Disabilities; Memory Weaknesses; Sensory Integration Disorders; Language problems.</p>

  <div class="brand brand--back"><span class="brand-dot"></span><span><span class="brand-name">Brightpath</span><span class="brand-name">Learning Center</span></span></div>
  <address class="return-address">1820 Maple Grove Ave.<br>Springfield, IL 62704</address>
  <div class="stamp-box" aria-label="Stamp area"></div>

  <div class="address-line" style="top:183px;"></div>
  <div class="address-line" style="top:219px;"></div>
  <div class="address-line" style="top:255px;"></div>
  <div class="address-line" style="top:291px;"></div>
  <div class="address-line" style="top:327px;"></div>

  <footer class="contact-band">brightpathtutoring.com<span class="sep"></span>555-014-2290<span class="sep"></span>info@BrightpathTutoring.com</footer>
</section>

</body>
</html>
```